PowerPoint Presentation for Digital Strategy

I have a PPT that needs consistent graphics, images, text clean-up, concise flow, etc.

Tallmark Advisory is based in Chicago and preparing a presentation to University Bookstores and staff on the benefits of doing an FULL-COVERage model that will lower costs to students.

The pitch includes case studies that show a savings to students on the cost of using digital textbooks over the traditional print textbooks.

Bookstores need to be in the middle of the process and offer course materials included with tuition so that the books will be available on the first day of class. Having the materials shows proof of improved learning outcomes.

Target Market(s)

Universities and University Bookstores

Industry/Entity Type

Education

Requirements
Must have
• Clear, concise flow, charts, images, graphics

```html
<!DOCTYPE html>
<html lang="en">
<head>
<meta charset="utf-8">
<title>The Ready Program at NPSU – The Challenge</title>
<link rel="stylesheet" href="https://fonts.googleapis.com/css2?family=Raleway:ital,wght@0,300;0,600;0,800;1,300&display=swap">
<style>
  :root {
    --green: #97c83e;
    --ink: #3e3c31;
    --paper: #ffffff;
    --placeholder: #e4e3dd;
  }
  * { margin: 0; padding: 0; box-sizing: border-box; }
  html, body {
    width: 1200px;
    height: 675px;
    overflow: hidden;
    background: var(--paper);
  }
  .slide {
    position: relative;
    width: 1200px;
    height: 675px;
    background: var(--paper);
    font-family: "Raleway", sans-serif;
    color: var(--ink);
  }
  .slide-title {
    position: absolute;
    left: 34px;
    top: 32px;
    font-weight: 800;
    font-size: 88px;
    line-height: 1;
    color: var(--green);
    letter-spacing: 0.5px;
    white-space: nowrap;
  }
  .slide-subtitle {
    position: absolute;
    left: 45px;
    top: 118px;
    font-weight: 300;
    font-style: italic;
    font-size: 44px;
    line-height: 1;
    color: var(--ink);
  }
  .challenge-card {
    position: absolute;
    left: 38px;
    top: 254px;
    width: 641px;
    height: 335px;
    border: 2px solid var(--green);
  }
  .challenge-heading {
    position: absolute;
    left: 25px;
    top: 42px;
    font-weight: 300;
    font-size: 72px;
    line-height: 1;
    color: var(--green);
    white-space: nowrap;
  }
  .challenge-rule {
    position: absolute;
    left: 26px;
    top: 125px;
    width: 584px;
    height: 3px;
    background: var(--green);
  }
  .challenge-text {
    position: absolute;
    left: 28px;
    top: 142px;
    width: 600px;
    font-weight: 600;
    font-size: 33px;
    line-height: 36.5px;
    color: var(--ink);
    white-space: nowrap;
  }
  .waiting-student {
    position: absolute;
    left: 764px;
    top: 228px;
    width: 295px;
    height: 354px;
  }
</style>
</head>
<body>
  <main class="slide">
    <h1 class="slide-title">THE READY PROGRAM</h1>
    <p class="slide-subtitle">at NPSU</p>

    <section class="challenge-card">
      <h2 class="challenge-heading">THE CHALLENGE</h2>
      <div class="challenge-rule"></div>
      <p class="challenge-text">Students waiting several weeks into<br>the semester to purchase their<br>course materials, resulting in<br>negative impacts on instruction time</p>
    </section>

    <svg class="waiting-student" viewBox="0 0 295 354" role="img" aria-label="Icon of a student seated at a desk next to a wall clock, waiting">
      <rect x="0" y="0" width="295" height="354" fill="var(--placeholder)"/>
    </svg>
  </main>
</body>
</html>
```